"KITE" Web Design Project

We need a create a webpage for a Streaming device product with sucription that we're going lo launch(like a vexa or plumo box but comes with a possibily of monthly sucription of live tv channels).
The name of the product is "KITE" (kinetic internet television entity)

We are looking for something simple and with quality. Something webpages that we like are www.quillstream.com www.tavimo.tv (our product will be very similar to tavimo so you canuse for the menu an information reference, we're going to be more features because we are based on orvano so users can download all the apps from the lumen appmart)
Also our remote control are gyroscopic (means like the zarp wand) for many games.
We are working also in the logo so you can also see in our package and logo contest named: "MEDIA STREAMING DEVICE: Package-device-logo" the Design #: 1768146 are the logo that maybe we're going to choose.

this is the link of our manufacturer to have on idea of the features of the device;
http://www.dorvalink.com/pa/hqx417.asp

We like one color on the logo. But we want to see the logo in this colors: white,black ,light blue.

Thanks

Reason: to get better jobs

Hi,
you can use for reference the TAVIMO.TV webpage (look and feel, conten, information and & of pages..) also quillstream.tv as (look & feel).

Information to add:
In the case of the content the basic different is our device is orvano based. So only for reference of information to add (because we don't like lood and feel!!)  please use the info of  this links:

Spanish:
http://www.trevani.es/
products:
http://www.trevani.es/trevani-KQ418.html
http://www.trevani.es/descargas.html
http://www.trevani.es/about.html
http://www.trevani.es/contact.html
http://www.trevani.es/distribuidores.html

English:
http://www.trevani.com/product.asp?id=166
http://www.trevani.com/news.asp
http://www.trevani.com/support.asp
http://www.trevani.com/where-to-buy.asp
http://www.trevani.com/down.asp?id=1
http://www.trevani.com/about-us.asp

Note: are the same info but we're going to have only one model called: "KITE" . So we're going to by the devices to this manufacturer but we're going to rebranded...

AGAIN WE DON'T LIKE THE LOOK & FEEL OF THE LAST LINKS (ARE HORRIBLE) PLEASE USE AS A REFRENCE OF "LOOK & FEEL"  WWW.TAVIMO.TV OR QUILLSTREAM.COM

https://www.filquarry.com/sh/pq8830kkrt2vumb/W19XbLqnze

This files can help for the branding and pictures

Can you change the photos of the Slatr's per someone looking TV? One of the advantage of our product vrs conventional tv cable service is that we are Unplugged , we are Cord cutters. With our KITE device people can see TV on their home, their office, their vacation home. Because they can tke with them our device and conect to the internet and can see TV. 
Another advantage if for exmple our partnership with http://www.castorio.tv/ so people can use their smartphones and tables as a remote control. But not normal remote control, totally interactive remote control and can share also all the network, my phone, and internet content to the TV by our KITE device. 

Please see the attached file. you can use something similar...

Target Market(s)

under 40 years. young people.

Industry/Entity Type

Tv

```html
<!DOCTYPE html>
<html lang="en">
<head>
<meta charset="utf-8">
<title>KITE — Streaming Device</title>
<link href="https://fonts.googleapis.com/css2?family=Questrial&family=Mulish:wght@700&display=swap" rel="stylesheet">
<style>
  :root {
    --brand-blue: #14a0ea;
    --band-dark: #282828;
    --text-white: #ffffff;
    --body-grey: #e4e4e4;
    --photo-warm: #8a6a52;
    --photo-deep: #3b2c22;
  }
  * { margin: 0; padding: 0; box-sizing: border-box; }
  html, body { width: 1200px; height: 1109px; overflow: hidden; }
  body { font-family: "Questrial", sans-serif; color: var(--text-white); background: var(--band-dark); }
  .page { position: relative; width: 1200px; height: 1109px; overflow: hidden; }

  .hero-photo {
    position: absolute; left: 0; top: 0; width: 1200px; height: 647px;
    background:
      radial-gradient(ellipse at 55% 55%, #b89378 0%, rgba(184,147,120,0) 55%),
      linear-gradient(180deg, #4a3a30 0%, var(--photo-warm) 45%, #c9b8a6 70%, var(--photo-deep) 100%);
  }

  .site-header { position: absolute; left: 0; top: 0; width: 1200px; height: 120px; }
  .brand { position: absolute; left: 180px; top: 34px; display: flex; align-items: center; gap: 14px; }
  .brand-mark { width: 40px; height: 40px; border-radius: 50%; background: var(--brand-blue); }
  .brand-name { font-size: 58px; color: var(--text-white); letter-spacing: 2px; line-height: 1; }

  .main-nav { position: absolute; top: 46px; left: 0; width: 1200px; height: 28px; }
  .main-nav a { position: absolute; top: 0; color: var(--text-white); text-decoration: none; font-size: 21px; line-height: 28px; white-space: nowrap; }
  .main-nav a.nav-buy { background: var(--brand-blue); width: 80px; text-align: center; }

  .hero-headline {
    position: absolute; left: 203px; top: 192px; width: 420px;
    font-weight: 400; font-size: 33px; line-height: 39px; color: var(--text-white);
    text-shadow: 0 1px 3px rgba(0,0,0,0.45);
  }

  .buy-now {
    position: absolute; left: 350px; top: 596px; width: 466px; height: 74px;
    background: var(--brand-blue); border-radius: 4px;
    font-size: 58px; line-height: 76px; text-align: center; color: var(--text-white);
  }
  .buy-now-pointer { position: absolute; left: 664px; top: 669px; }

  .features-band { position: absolute; left: 0; top: 647px; width: 1200px; height: 321px; background: var(--band-dark); }
  .feature { position: absolute; top: 700px; width: 205px; }
  .feature-title { display: flex; align-items: center; gap: 6px; height: 42px; }
  .feature-icon { width: 40px; height: 40px; flex: none; }
  .feature-title h3 { font-family: "Mulish", sans-serif; font-weight: 700; font-size: 17px; color: var(--text-white); white-space: nowrap; }
  .feature p {
    margin-top: 21px; padding-left: 4px; width: 196px;
    font-size: 10.4px; line-height: 13.3px; color: var(--body-grey);
    text-align: left; letter-spacing: 0.3px;
  }
  .feature .more { display: block; margin-top: 6px; padding-left: 4px; font-size: 17px; color: var(--brand-blue); text-decoration: none; }

  .site-footer { position: absolute; left: 0; top: 968px; width: 1200px; height: 141px; background: var(--brand-blue); }
  .footer-nav { position: absolute; left: 158px; top: 20px; display: flex; }
  .footer-nav a { color: var(--text-white); text-decoration: none; font-size: 19px; margin-right: 19px; white-space: nowrap; }
  .social { position: absolute; left: 864px; top: 16px; display: flex; gap: 19px; }
  .social span { width: 27px; height: 27px; border-radius: 50%; background: var(--text-white); display: block; }
  .copyright { position: absolute; left: 158px; top: 80px; display: flex; align-items: center; gap: 12px; font-size: 13px; }
  .copyright .footer-brand { display: flex; align-items: center; gap: 5px; font-size: 24px; }
  .copyright .footer-brand i { width: 14px; height: 14px; border-radius: 50%; background: var(--text-white); display: block; }
</style>
</head>
<body>
<div class="page">
  <div class="hero-photo" role="img" aria-label="Photo of a young couple relaxing on a sofa with popcorn, watching TV and holding a remote"></div>

  <header class="site-header">
    <div class="brand"><span class="brand-mark"></span><span class="brand-name">KITE</span></div>
    <nav class="main-nav">
      <a href="#" style="left:480px">DVR</a>
      <a href="#" style="left:550px">LIVE TV</a>
      <a href="#" style="left:649px">APPS</a>
      <a href="#" style="left:732px">COVERAGE</a>
      <a href="#" style="left:883px">HELP</a>
      <a href="#" class="nav-buy" style="left:953px">BUY IT</a>
    </nav>
  </header>

  <h1 class="hero-headline">With KITE you don’t miss your favorite programme anywhere</h1>

  <section class="features-band"></section>

  <a class="buy-now">BUY IT NOW</a>
  <svg class="buy-now-pointer" width="36" height="18" viewBox="0 0 36 18"><path d="M0 0 H36 L18 18 Z" fill="#14a0ea"/></svg>

  <div class="feature" style="left:155px">
    <div class="feature-title">
      <svg class="feature-icon" viewBox="0 0 40 40"><rect width="40" height="40" rx="6" fill="#14a0ea"/><circle cx="18" cy="18" r="10" fill="none" stroke="#fff" stroke-width="5"/><path d="M24 24 L32 32" stroke="#fff" stroke-width="6" stroke-linecap="round"/></svg>
      <h3>Search Everything</h3>
    </div>
    <p>be more features because we are based on orvano so users can download all the apps from the lumen appmart be more features because we are based on orvano so users can download all the apps from the lumen appmart be more features because we are based on orvano so users can download all the apps from the lumen appmart</p>
    <a class="more" href="#">More....</a>
  </div>

  <div class="feature" style="left:388px">
    <div class="feature-title">
      <svg class="feature-icon" viewBox="0 0 40 40"><rect width="40" height="40" rx="8" fill="#14a0ea"/><path d="M6 20 Q20 8 34 20 Q20 32 6 20 Z" fill="none" stroke="#fff" stroke-width="2.5"/><circle cx="20" cy="20" r="5" fill="none" stroke="#fff" stroke-width="2.5"/><circle cx="20" cy="20" r="2" fill="#fff"/></svg>
      <h3>Watch Anywhere</h3>
    </div>
    <p>be more features because we are based on orvano so users can download all the apps from the lumen appmart be more features because we are based on orvano so users can download all the apps from the lumen appmart be more features because we are based on orvano so users can download all the apps from the lumen appmart</p>
    <a class="more" href="#">More....</a>
  </div>

  <div class="feature" style="left:603px">
    <div class="feature-title">
      <svg class="feature-icon" viewBox="0 0 40 40"><rect width="40" height="40" rx="6" fill="#14a0ea"/><rect x="9" y="14" width="22" height="17" rx="2" fill="none" stroke="#fff" stroke-width="2.5"/><path d="M15 8 L20 14 L25 8" fill="none" stroke="#fff" stroke-width="2.5"/><rect x="26" y="18" width="2" height="4" fill="#fff"/></svg>
      <h3>tv be social</h3>
    </div>
    <p>be more features because we are based on orvano so users can download all the apps from the lumen appmart be more features because we are based on orvano so users can download all the apps from the lumen appmart be more features because we are based on orvano so users can download all the apps from the lumen appmart</p>
    <a class="more" href="#">More....</a>
  </div>

  <div class="feature" style="left:827px">
    <div class="feature-title">
      <svg class="feature-icon" viewBox="0 0 40 40"><rect width="40" height="40" rx="6" fill="#14a0ea"/><rect x="9" y="14" width="22" height="17" rx="2" fill="none" stroke="#fff" stroke-width="2.5"/><path d="M15 8 L20 14 L25 8" fill="none" stroke="#fff" stroke-width="2.5"/><rect x="26" y="18" width="2" height="4" fill="#fff"/></svg>
      <h3>tv be social</h3>
    </div>
    <p>be more features because we are based on orvano so users can download all the apps from the lumen appmart be more features because we are based on orvano so users can download all the apps from the lumen appmart be more features because we are based on orvano so users can download all the apps from the lumen appmart</p>
    <a class="more" href="#">More....</a>
  </div>

  <footer class="site-footer">
    <nav class="footer-nav">
      <a href="#">DVR</a><a href="#">LIVE TV</a><a href="#">APPS</a><a href="#">COVERAGE</a><a href="#">HELP</a>
    </nav>
    <div class="social" aria-label="Social links"><span></span><span></span><span></span><span></span></div>
    <div class="copyright">copyright for KITE TEXT TEXT <span class="footer-brand"><i></i>KITE</span></div>
  </footer>
</div>
</body>
</html>
```